Klassisches Visitenkarten-Design mit braunen Farbtönen gesucht
Zielgruppe
Meine Firma bietet Pferdezahnbehandlungen, Pferdefütterungsberatung sowie Trensen- und Gebissanpassungen an. Ausserdem habe ich eine mobile Pferdewaage. Meine Kunden sind Pferdebesitzer der gehobenen Klasse, die gerne Geld in die Hand nehmen um ihr Tier korrekt zu halten/versorgen.
Ich setze bisher auf ein klassisches Design in braun Tönen.
Aufgabenstellung
Mir ist eine klare, schnörkellose Botschaft wichtig.
Ich möchte mich gerne mit klassischem, aber auch sehr schönem Design von der Konkurrenz abheben.
Der Fokus soll auf der wissenschaftlichen Arbeitsweise mit dem Partner Pferd liegen.
Im Anhang sind Fotos von der alten Visitenkarten. Dort fehlt mir aber die klare Linie.
Normalerweise arbeite ich mit der Schriftart Eurostyle, bin aber auch für neue Vorschläge offen.

```html
<!DOCTYPE html>
<html lang="de">
<head>
<meta charset="utf-8">
<title>HIPPONOVA – Visitenkarte</title>
<link href="https://fonts.googleapis.com/css2?family=Saira:wght@400;600;700&display=swap" rel="stylesheet">
<style>
  :root {
    --canvas: #ededed;
    --card: #ffffff;
    --text-grey: #737373;
    --brown-dark: #542d12;
    --brown-mid: #9a7250;
    --beige-faint: #e6dcd3;
  }
  * { margin: 0; padding: 0; box-sizing: border-box; }
  html, body {
    width: 1200px; height: 1200px; overflow: hidden;
    background: var(--canvas);
    font-family: "Saira", "Helvetica Neue", Arial, sans-serif;
    color: var(--text-grey);
  }
  .card {
    position: absolute; left: 238px; width: 723px; height: 468px;
    background: var(--card); overflow: hidden;
  }
  .card--front { top: 80px; }
  .card--back { top: 642px; }

  .contact { position: absolute; left: 116px; top: 50px; }
  .contact__name { font-size: 27px; font-weight: 700; line-height: 1; }
  .contact__role { margin-top: 26px; font-size: 21px; font-weight: 700; line-height: 24px; }
  .contact__address, .contact__channels { font-size: 21px; font-weight: 400; line-height: 24px; }
  .contact__address { margin-top: 24px; }
  .contact__channels { margin-top: 24px; }

  .services {
    position: absolute; font-weight: 700; white-space: nowrap;
  }
  .card--front .services { left: 116px; top: 383px; font-size: 17.5px; letter-spacing: 0.2px; }
  .card--back .services { left: 0; right: 0; top: 400px; text-align: center; font-size: 19.5px; letter-spacing: 0.2px; }

  .brand {
    position: absolute; display: flex; flex-direction: column; align-items: center;
    color: var(--brown-dark); font-weight: 700; letter-spacing: 1px; line-height: 1;
  }
  .brand__dot { display: block; border-radius: 50%; background: var(--brown-dark); }
  .card--front .brand { left: 467px; width: 240px; top: 45px; gap: 22px; font-size: 30px; }
  .card--front .brand__dot { width: 175px; height: 175px; }
  .card--back .brand { left: 0; right: 0; top: 40px; gap: 26px; font-size: 40px; }
  .card--back .brand__dot { width: 220px; height: 220px; }

  .decor-circle {
    position: absolute; left: -70px; top: 285px; width: 175px; height: 175px;
    border-radius: 50%; background: var(--beige-faint);
  }
</style>
</head>
<body>
  <section class="card card--front">
    <div class="decor-circle" aria-hidden="true"></div>
    <div class="contact">
      <p class="contact__name">Marlene S. Ackermann</p>
      <p class="contact__role">Agrarwissenschaften (Dr. sc.)<br>HIPPONOVA</p>
      <p class="contact__address">Lindenweg 12<br>79868 Tannau/Hochschwarzwald</p>
      <p class="contact__channels">Telefon: +49 (0) 170 - 5550182<br>E-Mail: post@zahnpferd-beratung.de<br>Internet: www.hipponova.de</p>
    </div>
    <div class="brand"><span class="brand__dot"></span>HIPPONOVA</div>
    <p class="services">Pferdezahnbehandlung&nbsp; * &nbsp;Pferdefütterungsberatung&nbsp; * &nbsp;Pferdewaage</p>
  </section>

  <section class="card card--back">
    <div class="brand"><span class="brand__dot"></span>HIPPONOVA</div>
    <p class="services">Pferdezahnbehandlung&nbsp; * &nbsp;Pferdefütterungsberatung&nbsp; * &nbsp;Pferdewaage</p>
  </section>
</body>
</html>
```